Letterhead Design Project

Professional but modern letterhead.

Target Market(s)

mining companies

Industry/Entity Type

It Professional

Colors

Designer to choose colors to be used in the design.

```html
<!DOCTYPE html>
<html lang="en">
<head>
<meta charset="utf-8">
<title>KELVO Stationery Set</title>
<link rel="stylesheet" href="https://fonts.googleapis.com/css2?family=Questrial&display=swap">
<style>
  :root {
    --backdrop: #404040;
    --brand-blue: #2b5291;
    --cream: #fbfbe8;
    --paper: #ffffff;
    --ghost: #e6e6e6;
    --edge: #a9a9a9;
  }
  html, body { margin: 0; padding: 0; overflow: hidden; background: var(--backdrop); }
  .stationery-board { display: block; width: 1200px; height: 1029px; }
  .stationery-board text { font-family: "Questrial", "Century Gothic", sans-serif; }
  .sheet-cream { fill: var(--cream); }
  .sheet-white { fill: var(--paper); }
  .band-blue { fill: var(--brand-blue); }
  .ghost-mark { fill: var(--ghost); }
  .brand-name { fill: var(--brand-blue); font-size: 24px; }
  .brand-name--small { font-size: 17px; }
  .brand-name--white { fill: var(--paper); }
  .brand-square { fill: var(--brand-blue); }
  .brand-square--white { fill: var(--paper); }
  .contact-line { font-size: 6.6px; fill: var(--brand-blue); }
  .contact-line--white { fill: var(--paper); }
  .contact-label { font-weight: 700; }
  .holder-name { font-size: 13px; fill: var(--paper); }
  .holder-name--blue { fill: var(--brand-blue); }
  .rule { stroke: var(--brand-blue); stroke-width: 1; }
</style>
</head>
<body>
<svg class="stationery-board" viewBox="0 0 1167 1000" preserveAspectRatio="none" xmlns="http://www.w3.org/2000/svg">
  <defs>
    <clipPath id="folder-left-clip"><rect x="113" y="8" width="268" height="380"/></clipPath>
    <clipPath id="sleeve-clip"><rect x="35" y="688" width="317" height="299"/></clipPath>
    <clipPath id="sheet-clip"><rect x="773" y="433" width="378" height="551"/></clipPath>
  </defs>

  <!-- Presentation folder: inside left panel -->
  <g class="folder-left">
    <rect class="sheet-cream" x="113" y="8" width="268" height="380"/>
    <g clip-path="url(#folder-left-clip)">
      <circle class="ghost-mark" cx="230" cy="300" r="120" role="img" aria-label="Faint brand decoration"/>
    </g>
  </g>

  <!-- Folder flap, left -->
  <g class="folder-side-flap">
    <path class="sheet-cream" d="M105 218 L105 388 L55 355 L17 355 L17 255 L55 255 Z"/>
    <path class="band-blue" d="M17 255 L55 255 L105 218 L105 290 C62 292 32 305 17 325 Z"/>
  </g>

  <!-- Folder cover panel -->
  <g class="folder-cover">
    <rect class="sheet-cream" x="388" y="8" width="269" height="380"/>
    <path class="band-blue" d="M388 388 C420 352 520 360 600 352 C640 348 655 336 657 320 L657 388 Z"/>
    <rect class="brand-square" x="515" y="160" width="16" height="16"/>
    <text class="brand-name" x="523" y="250" text-anchor="middle" font-size="30">KELVO</text>
  </g>

  <!-- Folder pocket with card slot -->
  <g class="folder-pocket">
    <path class="sheet-cream" d="M113 397 L381 397 C370 420 352 470 334 505 C322 528 300 530 250 535 C190 542 150 558 125 550 C112 540 113 470 113 397 Z"/>
    <rect class="band-blue" x="198" y="436" width="100" height="56"/>
  </g>

  <!-- Business card, front -->
  <g class="business-card business-card--front">
    <rect class="sheet-cream" x="739" y="5" width="351" height="190"/>
    <path class="band-blue" d="M900 195 C920 150 960 142 1020 136 C1062 131 1085 112 1090 80 L1090 195 Z"/>
    <rect class="brand-square" x="1035" y="24" width="14" height="14"/>
    <text class="brand-name" x="1042" y="95" text-anchor="middle">KELVO</text>
    <text class="contact-line" x="755" y="132"><tspan class="contact-label">Address:</tspan> Suite #118, Ore Hall,</text>
    <text class="contact-line" x="780" y="141">NY 40712</text>
    <text class="contact-line" x="755" y="150"><tspan class="contact-label">Tel:</tspan> 555-210-4478</text>
    <text class="contact-line" x="755" y="160"><tspan class="contact-label">Mobile:</tspan> 555-389-6621</text>
    <text class="contact-line" x="755" y="170"><tspan class="contact-label">e-mail:</tspan> hello@kelvoworks.com</text>
    <text class="contact-line" x="755" y="180"><tspan class="contact-label">Web:</tspan> www.kelvoworks.com</text>
    <text class="holder-name" x="956" y="174">Aaron Blake | CEO</text>
  </g>

  <!-- Business card, back -->
  <g class="business-card business-card--back">
    <rect class="band-blue" x="739" y="218" width="351" height="190"/>
    <path class="sheet-white" d="M900 408 C920 363 960 355 1020 349 C1062 344 1085 325 1090 293 L1090 408 Z"/>
    <rect class="brand-square--white" x="1035" y="237" width="14" height="14"/>
    <text class="brand-name brand-name--white" x="1042" y="308" text-anchor="middle">KELVO</text>
    <text class="contact-line contact-line--white" x="755" y="345"><tspan class="contact-label">Address:</tspan> Suite #118, Ore Hall,</text>
    <text class="contact-line contact-line--white" x="780" y="354">NY 40712</text>
    <text class="contact-line contact-line--white" x="755" y="363"><tspan class="contact-label">Tel:</tspan> 555-210-4478</text>
    <text class="contact-line contact-line--white" x="755" y="373"><tspan class="contact-label">Mobile:</tspan> 555-389-6621</text>
    <text class="contact-line contact-line--white" x="755" y="383"><tspan class="contact-label">e-mail:</tspan> hello@kelvoworks.com</text>
    <text class="contact-line contact-line--white" x="755" y="393"><tspan class="contact-label">Web:</tspan> www.kelvoworks.com</text>
    <text class="holder-name holder-name--blue" x="956" y="387">Aaron Blake | CEO</text>
  </g>

  <!-- Disc and sleeve -->
  <g class="disc">
    <circle class="band-blue" cx="195" cy="710" r="150" stroke="var(--edge)" stroke-width="3"/>
    <rect class="brand-square--white" x="188" y="600" width="14" height="14"/>
    <text class="brand-name brand-name--white brand-name--small" x="195" y="634" text-anchor="middle">KELVO</text>
  </g>
  <g class="disc-sleeve">
    <rect class="sheet-cream" x="35" y="688" width="317" height="299"/>
    <path d="M157 688 A38 38 0 0 1 233 688" fill="var(--brand-blue)" stroke="var(--edge)" stroke-width="2"/>
    <circle class="sheet-white" cx="195" cy="710" r="19"/>
    <rect class="sheet-cream" x="150" y="720" width="90" height="10"/>
    <g clip-path="url(#sleeve-clip)">
      <circle class="ghost-mark" cx="150" cy="900" r="110" role="img" aria-label="Faint brand decoration"/>
    </g>
    <path class="band-blue" d="M210 987 C270 960 330 905 352 857 L352 987 Z"/>
    <rect class="brand-square--white" x="314" y="936" width="14" height="14"/>
    <text class="brand-name brand-name--white brand-name--small" x="321" y="970" text-anchor="middle">KELVO</text>
  </g>

  <!-- Letterhead -->
  <g class="letterhead">
    <rect class="sheet-white" x="385" y="432" width="382" height="554"/>
    <rect class="brand-square" x="416" y="465" width="14" height="14"/>
    <line class="rule" x1="449" y1="455" x2="449" y2="491"/>
    <text class="brand-name brand-name--small" x="456" y="479">KELVO</text>
    <line x1="435" y1="953" x2="716" y2="953" stroke="#e3e3e3" stroke-width="1"/>
  </g>

  <!-- Letterhead second sheet -->
  <g class="continuation-sheet">
    <rect class="sheet-cream" x="773" y="433" width="378" height="551"/>
    <g clip-path="url(#sheet-clip)">
      <circle class="ghost-mark" cx="940" cy="840" r="170" role="img" aria-label="Faint brand decoration"/>
    </g>
    <rect class="brand-square" x="1087" y="462" width="16" height="16"/>
    <text class="brand-name" x="1095" y="544" text-anchor="middle" font-size="27">KELVO</text>
  </g>
</svg>
</body>
</html>
```